Job advertisement design

We need an ad design template.
Format: 1/2 page landscape, bleed format: 210 x 136 mm, type area format: 177 x 120 mm
Please design and font accordingly “Flyer back and front”.
Text blocks (examples) see Word doc (can be shortened within the areas if there is too much text).
A template with writable text fields is required so that we can adapt the display independently in the future.

```html
<!DOCTYPE html>
<html lang="de">
<head>
<meta charset="utf-8">
<title>Stellenanzeige Geschäftsführung – Flyer Vorder- und Rückseite</title>
<link href="https://fonts.googleapis.com/css2?family=Arimo:wght@400;700&family=Archivo:wght@700;800&display=swap" rel="stylesheet">
<style>
  :root {
    --stage: #dadada;
    --slate: #4a5259;
    --sky: #c9e6f3;
    --paper: #ffffff;
    --ink: #1e1e1e;
    --heading: #3f5b8f;
    --photo-a: #dcd6cf;
    --photo-b: #9fb0bd;
    --photo-c: #c6d2dc;
    --photo-d: #7f8e99;
  }
  * { box-sizing: border-box; margin: 0; padding: 0; }
  html, body { width: 1200px; height: 768px; overflow: hidden; }
  body {
    background: var(--stage);
    font-family: "Arimo", Arial, sans-serif;
    color: var(--ink);
    position: relative;
  }
  .page {
    position: absolute;
    top: 42px;
    height: 684px;
    background: linear-gradient(var(--slate) 0 366px, var(--sky) 366px 100%);
    overflow: hidden;
  }
  .page--front { left: 139px; width: 441px; }
  .page--back { left: 618px; width: 443px; }

  .abs { position: absolute; }

  .logo-box {
    left: 41px; top: 70px; width: 70px; height: 82px;
    border: 1px solid #cfd3d6;
    color: #fff;
    font-family: "Archivo", Arial, sans-serif;
    font-weight: 800;
    font-size: 15px;
    line-height: 14px;
    padding: 27px 0 0 11px;
  }
  .photo-team-laptop {
    left: 222px; top: 0; width: 195px; height: 300px;
    background: linear-gradient(180deg, var(--photo-a) 0 30%, var(--photo-c) 55%, var(--photo-b) 100%);
  }
  .intro-panel {
    left: 31px; top: 230px; width: 410px; height: 246px;
    background: var(--paper);
  }
  .page--front .photo-team-laptop { z-index: 2; }
  .intro-text {
    left: 49px; top: 253px; width: 380px;
    font-size: 10.3px; font-weight: 700; line-height: 14.8px;
    z-index: 3;
  }
  .intro-text p + p { margin-top: 14.8px; }
  .intro-text .narrow { display: block; width: 175px; }

  .section-title {
    font-family: "Archivo", Arial, sans-serif;
    font-weight: 700;
    font-size: 15.5px;
    color: var(--heading);
    letter-spacing: 0.2px;
  }
  .bullet-list {
    list-style: none;
    font-size: 9.9px;
    line-height: 14.8px;
  }
  .bullet-list li { padding-left: 8px; text-indent: -8px; }
  .bullet-list li::before { content: "• "; }

  .expect-title { left: 35px; top: 504px; }
  .expect-list { left: 36px; top: 522px; width: 400px; }
  .expect-list li { padding-left: 10px; text-indent: -10px; }

  .profile-panel {
    left: 35px; top: 59px; width: 408px; height: 417px;
    background: var(--paper);
  }
  .bring-title { left: 40px; top: 84px; }
  .bring-list { left: 40px; top: 104px; width: 400px; }
  .tasks-title { left: 40px; top: 226px; }
  .tasks-list { left: 40px; top: 246px; width: 400px; }
  .photo-team-corridor {
    left: 215px; top: 324px; width: 228px; height: 152px;
    background: linear-gradient(160deg, var(--photo-c), var(--photo-d) 60%, var(--photo-c));
  }

  .contact-heading {
    left: 70px; top: 485px; width: 330px;
    font-family: "Archivo", Arial, sans-serif;
    font-weight: 700; font-size: 12.5px; line-height: 15px;
    color: var(--heading); letter-spacing: 0.3px;
  }
  .contact-card {
    left: 106px; top: 520px; width: 274px; height: 97px;
    background: var(--slate); border-radius: 3px;
    color: #fff; font-size: 9.9px; line-height: 11px;
  }
  .contact-portrait {
    left: 34px; top: 517px; width: 106px; height: 106px;
    border-radius: 50%; border: 2px solid #fff;
    background: radial-gradient(circle at 50% 45%, #8a8a8a, #2a2a2a 75%);
    z-index: 2;
  }
  .contact-name { left: 47px; top: 9px; }
  .contact-row { left: 47px; display: flex; align-items: center; gap: 11px; }
  .contact-row svg { width: 20px; height: 20px; flex: none; }
  .row-phone { top: 40px; }
  .row-mail { top: 60px; }
  .contact-web { left: 47px; top: 83px; }
</style>
</head>
<body>

<section class="page page--front" aria-label="Vorderseite">
  <div class="abs logo-box">LOGO<br>HERE</div>
  <div class="abs photo-team-laptop" role="img" aria-label="Foto: zwei Ärzte arbeiten gemeinsam am Laptop"></div>
  <div class="abs intro-panel"></div>
  <div class="abs intro-text">
    <p><span class="narrow">Im Auftrag unseres Kunden suchen wir im Rahmen einer strukturierten Altersnachfolge die Geschäftsführung (w/m/d)</span>für das Klinikum St. Elisabeth in Nordhafen.</p>
    <p>Der Träger Die Caritia Nord gGmbH ist eine regionale Betriebsgesellschaft der Caritia Deutschland gGmbH mit dem Ziel, die ganzheitliche Lösung für alle medizinischen Anliegen in dieser Region aus einer Hand darzustellen:<br>von der Gesundheitsvorsorge, der stationären sowie ambulanten Behandlung im Krankenhaus über die Rehabilitation, bis hin zur Versorgung und Pflege zu Hause oder in Altenpflegeeinrichtungen.</p>
  </div>

  <h2 class="abs section-title expect-title">Was Sie erwartet</h2>
  <ul class="abs bullet-list expect-list">
    <li>Möglichkeit, ein erfolgreiches, traditionsreiches Krankenhaus durch die gesundheitspolitischen Herausforderungen der kommenden Jahre zu führen</li>
    <li>Die Chance, Ihre Ideen und Konzepte einer zukunftsweisenden Gesundheitsversorgung in dem Fusionsprojekt einzubringen</li>
    <li>Flache Hierarchien sowie eine moderne und unbürokratische Arbeitsatmosphäre</li>
    <li>Ein attraktives finanzielles Vergütungspaket</li>
  </ul>
</section>

<section class="page page--back" aria-label="Rückseite">
  <div class="abs profile-panel"></div>

  <h2 class="abs section-title bring-title">Was Sie mitbringen</h2>
  <ul class="abs bullet-list bring-list">
    <li>Abgeschlossenes betriebswirtschaftliches Studium mit Schwerpunkt Gesundheitsökonomie bzw. Krankenhausbetriebswirtschaft oder eine vergleichbare Qualifikation</li>
    <li>Mehrjährige Leitungserfahrung in der Gesundheitswirtschaft, idealerweise im Krankenhausmanagement</li>
    <li>Ausgeprägte Planungs- und Steuerungskompetenz</li>
    <li>Kommunikationsstarke und charismatische Persönlichkeit</li>
  </ul>

  <h2 class="abs section-title tasks-title">Was Sie umsetzen</h2>
  <ul class="abs bullet-list tasks-list">
    <li>Strategisches und operatives Führen des Krankenhauses</li>
    <li>Erfolgreiches Umsetzen von Digitalisierungsprojekten und Change-Management</li>
    <li>Erstellung, Abstimmung und Umsetzung eines zukunftsfähigen Konzepts für Medizin, Pflege &amp; Verwaltung mit dem Fusionspartner</li>
  </ul>

  <div class="abs photo-team-corridor" role="img" aria-label="Foto: Team aus Ärztinnen und Ärzten im Klinikflur"></div>

  <p class="abs contact-heading">Für weitere Informationen sprechen Sie<br>uns gerne direkt an – wir freuen uns auf Sie:</p>

  <div class="abs contact-card">
    <p class="abs contact-name">Matthias Berger lindqvist.<br>Beratung im Gesundheitswesen</p>
    <div class="abs contact-row row-phone">
      <svg viewBox="0 0 20 20" aria-hidden="true"><circle cx="10" cy="10" r="10" fill="#fff"/><path d="M7 5.5c.6-.4 1.2-.2 1.5.4l.7 1.4c.2.5.1 1-.3 1.3l-.6.5c.5 1.2 1.4 2.1 2.6 2.6l.5-.6c.3-.4.8-.5 1.3-.3l1.4.7c.6.3.8.9.4 1.5-.7 1-1.8 1.4-2.9 1-2.6-.9-4.6-2.9-5.5-5.5-.4-1.1 0-2.2.9-3z" fill="#1e1e1e"/></svg>
      <span>+49 170 000 12 34</span>
    </div>
    <div class="abs contact-row row-mail">
      <svg viewBox="0 0 20 20" aria-hidden="true"><circle cx="10" cy="10" r="10" fill="#fff"/><rect x="5" y="6.5" width="10" height="7" rx="1" fill="#1e1e1e"/><path d="M5.6 7.2 10 10.6l4.4-3.4" stroke="#fff" stroke-width="1" fill="none"/></svg>
      <span>mb@beispielberatung.de</span>
    </div>
    <p class="abs contact-web">www.beratung-lindqvist.de</p>
  </div>
  <div class="abs contact-portrait" role="img" aria-label="Porträtfoto des Ansprechpartners in Schwarz-Weiß"></div>
</section>

</body>
</html>
```